New Web Page Design - Cement Rendering Business

Looking for a overhaul of our existing website (www.norpex.com.au).

Looking for a sleek and elegant design that incorporates the colours of our logos, black / green and white. Needs to look professional and want it to be well above what our competition is offering. (Findora search for 'cement rendering sydney' will display the competition we want to be well ahead of.

Prefer a mixture of pages with black background and white alternatively between home (black), about us (white), contact us (black) and gallery (white).

Would like to incorporate our logo on all pages attached preferably in the top left corner.

Website needs to be search engine optimised and have easily updated photo gallery which we already have.

Also need to embed our trackwise metrics code on the front home page.

Website needs to be able easily updated (text, pictures ) as required.
content management system should include fields where you can alter your page titles, meta description and keywords.

Pages also needs to be optimised for mobile devices, iphone, ipad and other mobile devices. (it is a current feature we have)

If you have any questions, just message me.

Please remember the look and feel of the site is important to us, we don't want it over complicated, simple elegant and professional in line with our logo standards.
Updates

Hi All, As an example of the look and feel we like. We have found a site that may assist in your design and creative process. http://demo.quorvix.org/ We like the simplicity, elegance and professional look of this site, although we would like it with our images, colours and logos. I hope this helps.! keep the great designs coming!

All, Thanks for the designs. Please try and use our website images due to copyright reasons for all your designs. Tomas

Target Market(s)

Construction Companies

Industry/Entity Type

Business

Colors
9bcb3b
acd036
474747

Requirements
Must have
• Search Engine Optimised.
Photo Gallery
Elegant/Professional Look & Feel.
Simple Yet Effective
Nice to have
• Moving Parts
Should not have
• Overly Complicated.
Cheap & Traditional Looking.
Boring

```html
<!DOCTYPE html>
<html lang="en">
<head>
<meta charset="utf-8">
<title>NORPEX Cement Rendering</title>
<link href="https://fonts.googleapis.com/css2?family=Quicksand:wght@400;500&family=Open+Sans:wght@400;600;700&display=swap" rel="stylesheet">
<style>
:root{
  --green:#9bcb3b;
  --ink:#222;
  --band:#333;
  --footer:#474747;
  --footer-bottom:#2e2e2e;
  --line:#e4e4e4;
  --white:#fff;
  --orange:#f07a2a;
  --wall:#9a9c9e;
}
*{margin:0;padding:0;box-sizing:border-box}
html,body{width:770px;height:1200px;overflow:hidden;background:var(--white)}
body{position:relative;font-family:"Open Sans",Arial,sans-serif;color:var(--ink)}
.abs{position:absolute}
.display{font-family:"Quicksand",Helvetica,sans-serif;font-weight:400}

/* header */
.site-header{left:0;top:0;width:770px;height:80px;border-bottom:1px solid var(--line);background:var(--white)}
.brand{left:72px;top:14px;display:flex;align-items:center;gap:10px}
.brand-dot{width:50px;height:50px;border-radius:50%;background:var(--green)}
.brand-name{font-family:"Quicksand",sans-serif;font-weight:400;font-size:30px;color:var(--ink);letter-spacing:.5px}
.main-nav{right:74px;top:31px;display:flex;gap:12px;align-items:center;font-family:"Quicksand",sans-serif;font-size:10.4px;font-weight:500}
.main-nav span{position:relative}
.main-nav .active{color:var(--green)}
.main-nav .active::before{content:"";position:absolute;left:-3px;right:-3px;top:-31px;height:2px;background:var(--green)}

/* hero */
.hero{left:0;top:80px;width:770px;height:294px;background:
  radial-gradient(ellipse 60px 90px at 40px 70px,rgba(240,110,30,.95),rgba(240,110,30,0) 100%),
  radial-gradient(ellipse 70px 55px at 300px 220px,rgba(250,170,40,.95),rgba(240,120,30,0) 100%),
  radial-gradient(ellipse 160px 40px at 140px 220px,rgba(190,120,90,.7),rgba(190,120,90,0) 100%),
  linear-gradient(125deg,rgba(0,0,0,0) 45%,rgba(200,200,200,.0) 45%),
  radial-gradient(ellipse 50px 130px at 400px 130px,rgba(205,205,205,.9),rgba(205,205,205,0) 100%),
  linear-gradient(90deg,#7d8185 0%,#8e9296 30%,#b9bbbc 52%,#e4e4e3 72%,#eeeeed 100%)}
.hero-title{left:438px;top:191px;font-size:21px;color:var(--ink)}
.hero-title b{color:var(--green);font-weight:500}
.hero-text{left:438px;top:222px;width:275px;font-size:9.8px;line-height:1.3;color:#444}
.btn{left:437px;top:261px;width:74px;height:25px;background:var(--green);color:var(--white);font-size:9.5px;font-weight:700;display:flex;align-items:center;justify-content:center}
.slide-arrow{top:210px;width:38px;height:40px;background:rgba(120,120,120,.75);display:flex;align-items:center;justify-content:center}

/* features */
.feature-icon{width:48px;height:48px;border-radius:50%;background:var(--green);top:418px;display:flex;align-items:center;justify-content:center}
.feature-title{top:414px;width:130px;font-size:12px;padding-bottom:2px;border-bottom:1.5px solid var(--green)}
.feature-text{top:439px;width:136px;font-size:8.2px;line-height:1.25}
.read-more{font-family:"Quicksand",sans-serif;font-size:10px;color:var(--green);text-decoration:underline}

/* band */
.band{left:0;top:558px;width:770px;height:137px;background:var(--band)}
.band-arrow{left:364px;top:694px}
.band-title{left:0;top:584px;width:770px;text-align:center;font-size:15px;color:var(--green)}
.band-text{left:92px;top:609px;width:586px;text-align:center;font-size:9.2px;line-height:1.38;color:var(--white)}

/* gallery */
.gallery-head{left:71px;top:740px;width:629px;height:41px;background:#f3f3f3;border-bottom:2px solid var(--line)}
.gallery-head h2{position:absolute;left:10px;top:11px;font-size:15px}
.gallery-nav{right:9px;top:7px;display:flex;gap:1px}
.gallery-nav span{width:22px;height:25px;background:#dcdcdc;display:flex;align-items:center;justify-content:center}
.card-photo{top:806px;width:186px;height:117px;box-shadow:0 0 0 3px #f0f0f0}
.photo-render{background:
  radial-gradient(ellipse 90px 60px at 40px 80px,rgba(240,110,80,.95),rgba(240,110,80,0) 100%),
  radial-gradient(ellipse 40px 30px at 140px 55px,rgba(80,80,80,.6),rgba(80,80,80,0) 100%),
  linear-gradient(110deg,#e27059 0%,#c9a393 45%,#c7c3bb 65%,#aeaba5 100%)}
.photo-vehicle{background:
  radial-gradient(ellipse 70px 45px at 100px 75px,rgba(250,250,250,1),rgba(250,250,250,0) 100%),
  radial-gradient(ellipse 40px 20px at 30px 70px,rgba(60,90,50,.8),rgba(60,90,50,0) 100%),
  linear-gradient(180deg,#3b6fb3 0%,#7d9cc4 30%,#c8cdd2 50%,#6e6c66 85%,#3e3d3a 100%)}
.photo-location{background:
  radial-gradient(ellipse 60px 40px at 60px 30px,rgba(160,90,55,.9),rgba(160,90,55,0) 100%),
  radial-gradient(ellipse 45px 25px at 110px 85px,rgba(110,85,70,.8),rgba(110,85,70,0) 100%),
  linear-gradient(120deg,#8b6a58 0%,#a79a90 35%,#bcbab6 65%,#a09e9a 100%)}
.card-label{top:807px;height:28px;padding:0 7px;background:rgba(30,30,30,.9);color:var(--white);font-family:"Quicksand",sans-serif;font-size:9.5px;display:flex;align-items:center}
.card-text{top:940px;width:186px;font-size:8.3px;line-height:1.25}

/* footer */
.site-footer{left:0;top:1036px;width:770px;height:136px;background:var(--footer)}
.footer-brand{left:72px;top:1052px;display:flex;align-items:center;gap:10px}
.footer-brand .brand-name{color:var(--white)}
.footer-title{left:292px;top:1051px;font-size:12px;color:var(--white)}
.contact-list{left:270px;top:1073px;list-style:none;font-size:8.6px;color:var(--white)}
.contact-list li{height:12.8px;display:flex;align-items:center}
.contact-list .ico{width:22px;display:flex;justify-content:center}
.footer-nav{right:70px;top:1054px;font-size:8.5px;color:#cfcfcf}
.footer-bottom{left:0;top:1172px;width:770px;height:28px;background:var(--footer-bottom);color:var(--white);font-size:8.5px;display:flex;align-items:center;justify-content:center}
</style>
</head>
<body>

<header class="site-header abs">
  <div class="brand abs"><span class="brand-dot"></span><span class="brand-name">NORPEX</span></div>
  <nav class="main-nav abs">
    <span class="active">Home</span><span>How we work</span><span>Services</span><span>About Us</span><span>Photo Gallery</span><span>Contact Us</span>
    <svg width="9" height="10" viewBox="0 0 9 10"><circle cx="3.7" cy="3.7" r="2.8" fill="none" stroke="#222" stroke-width="1.4"/><line x1="5.8" y1="5.8" x2="8.3" y2="8.6" stroke="#222" stroke-width="1.6"/></svg>
  </nav>
</header>

<section class="hero abs" role="img" aria-label="Gloved hand applying cement render to a wall with a trowel"></section>
<div class="slide-arrow abs" style="left:0"><svg width="10" height="16"><polyline points="8,1 2,8 8,15" fill="none" stroke="#fff" stroke-width="1.8"/></svg></div>
<div class="slide-arrow abs" style="left:732px"><svg width="10" height="16"><polyline points="2,1 8,8 2,15" fill="none" stroke="#fff" stroke-width="1.8"/></svg></div>
<h1 class="hero-title display abs">Welcome to <b>NORPEX</b></h1>
<p class="hero-text abs">We are an Australian owned and operated business with over 25 years of experience in our field.</p>
<a class="btn abs">READ MORE</a>

<section class="features">
  <div class="feature-icon abs" style="left:75px"><svg width="20" height="18"><polygon points="10,2 19,10 16,10 16,17 4,17 4,10 1,10" fill="none" stroke="#fff" stroke-width="1.6"/><rect x="8" y="11" width="4" height="6" fill="#fff"/></svg></div>
  <h3 class="feature-title display abs" style="left:133px">Residential Projects</h3>
  <p class="feature-text abs" style="left:134px">Lorem Ipsum is simply dummy text of the printing and typeset-ting industry. Lorem Ipsum has been the industry's standard dummy text ever since the 1500s</p>
  <a class="read-more abs" style="left:134px;top:506px">Read More</a>

  <div class="feature-icon abs" style="left:292px"><svg width="20" height="16"><path d="M2 3h6l2 2h8v10H2z" fill="none" stroke="#fff" stroke-width="1.6"/></svg></div>
  <h3 class="feature-title display abs" style="left:351px">Private Projects</h3>
  <p class="feature-text abs" style="left:352px">Lorem Ipsum is simply dummy text of the printing and typeset-ting industry. Lorem Ipsum has been the industry's standard dummy text ever since the 1500s</p>
  <a class="read-more abs" style="left:351px;top:506px">Read More</a>

  <div class="feature-icon abs" style="left:510px"><svg width="20" height="16"><rect x="5" y="1" width="10" height="4" fill="none" stroke="#fff" stroke-width="1.5"/><rect x="1" y="5" width="18" height="7" fill="none" stroke="#fff" stroke-width="1.5"/><rect x="5" y="10" width="10" height="5" fill="#fff"/></svg></div>
  <h3 class="feature-title display abs" style="left:569px">Commercial Projects</h3>
  <p class="feature-text abs" style="left:570px">Lorem Ipsum is simply dummy text of the printing and typeset-ting industry. Lorem Ipsum has been the industry's standard dummy text ever since the 1500s</p>
  <a class="read-more abs" style="left:569px;top:506px">Read More</a>
</section>

<section class="band abs"></section>
<svg class="band-arrow abs" width="36" height="17"><polygon points="0,0 36,0 18,17" fill="#333"/></svg>
<h2 class="band-title display abs">Your one stop shop for all your cement rendering needs</h2>
<p class="band-text abs">Our work is fully licensed, our employee's are trained to the highest standards and all of our work is covered by warranty.We offer an obligation free on-site consultation and quotation service for your convenience 7 days per week. We are the preferred supplier for many of the top building companies in Australia which gives you the access to our expertise, competetive rates and peace of mind.No job is too big or too small. We work on several residential, private and commercial projects all year round.</p>

<section class="gallery-head abs">
  <h2 class="display">Photo Gallery</h2>
  <div class="gallery-nav abs">
    <span><svg width="7" height="12"><polyline points="6,1 1,6 6,11" fill="none" stroke="#fff" stroke-width="1.5"/></svg></span>
    <span><svg width="7" height="12"><polyline points="1,1 6,6 1,11" fill="none" stroke="#fff" stroke-width="1.5"/></svg></span>
  </div>
</section>

<div class="card-photo photo-render abs" style="left:71px" role="img" aria-label="Worker in orange glove smoothing render with a trowel"></div>
<div class="card-label abs" style="left:71px">NORPEX Cement rendering</div>
<p class="card-text abs" style="left:71px">Lorem Ipsum is simply dummy text of the print-ing and typesetting industry. Lorem Ipsum has been the industry's standard dummy text ever since the 1500s</p>
<a class="read-more abs" style="left:71px;top:990px">Read More</a>

<div class="card-photo photo-vehicle abs" style="left:293px" role="img" aria-label="White company van parked on a street"></div>
<div class="card-label abs" style="left:293px">Our Vehicle</div>
<p class="card-text abs" style="left:293px">Lorem Ipsum is simply dummy text of the print-ing and typesetting industry. Lorem Ipsum has been the industry's standard dummy text ever since the 1500s</p>
<a class="read-more abs" style="left:293px;top:990px">Read More</a>

<div class="card-photo photo-location abs" style="left:515px" role="img" aria-label="Hand pressing a float trowel against a freshly rendered wall"></div>
<div class="card-label abs" style="left:515px">On Location</div>
<p class="card-text abs" style="left:515px">Lorem Ipsum is simply dummy text of the print-ing and typesetting industry. Lorem Ipsum has been the industry's standard dummy text ever since the 1500s</p>
<a class="read-more abs" style="left:515px;top:990px">Read More</a>

<footer class="site-footer abs"></footer>
<div class="footer-brand abs"><span class="brand-dot"></span><span class="brand-name">NORPEX</span></div>
<h3 class="footer-title display abs">Contact us</h3>
<ul class="contact-list abs">
  <li><span class="ico"></span>NORPEX Cement Rendering</li>
  <li><span class="ico"><svg width="8" height="8"><path d="M1 1l2 0 1 2-1 1a5 5 0 0 0 2 2l1-1 2 1 0 2c-4 0-7-3-7-7z" fill="#fff"/></svg></span>Phone: (02) 5550 1843</li>
  <li><span class="ico"><svg width="6" height="10"><rect x="0.5" y="0.5" width="5" height="9" rx="1" fill="none" stroke="#fff"/></svg></span>Mobile: 0400 555 218</li>
  <li><span class="ico"><svg width="10" height="7"><rect x="0.5" y="0.5" width="9" height="6" fill="#fff"/><polyline points="0.5,0.5 5,4 9.5,0.5" fill="none" stroke="#474747"/></svg></span>Email: works@norpex.com.au</li>
  <li><span class="ico"><svg width="10" height="7"><rect x="0" y="0" width="10" height="7" fill="#fff"/><rect x="5" y="2" width="3" height="3" fill="#474747"/></svg></span>Fax: (02) 5550 7319</li>
  <li><span class="ico"><svg width="9" height="9"><circle cx="4.5" cy="4.5" r="3.8" fill="none" stroke="#fff" stroke-width="1.2"/><line x1="0.7" y1="4.5" x2="8.3" y2="4.5" stroke="#fff"/><ellipse cx="4.5" cy="4.5" rx="1.6" ry="3.8" fill="none" stroke="#fff"/></svg></span>Web: www.norpex.com.au</li>
</ul>
<nav class="footer-nav abs">Home &nbsp;| &nbsp;Services &nbsp;| &nbsp;About Us &nbsp;| &nbsp;Photo Gallery &nbsp;| &nbsp;Contact Us</nav>
<div class="footer-bottom abs">© 2014 &nbsp;|&nbsp; all rights reserved &nbsp;|&nbsp; NORPEX</div>

</body>
</html>
```